C U B A N - C I G A R S - F L Y E R

I need a double-sided 5x7 club type flyer for a Memorial Day Weekend Trip.
The main side design needs to be similar to the attached flyer example. The front design of flyer is KEY. The design will be awarded to the closest finished submission to the example flyer.
Both sides of the flyer should also included event and business logo, which are also attached. Both logos can be altered to fit printing need accordingly.
Front side content is also attached.
The back side design will be very simple. Consists of 3 travel images and trip description, and my contact very details. Same color design as front. The attached word document contains backside details for REFERENCE ONLY. Please focus on front side when submitting a design for this project.
Target Market(s)
A F R I C A N - A M E R I C A N - C I G A R - S M O K E R S
Industry/Entity Type
Travel Industry
Requirements
Must have
- All the elements of the attached information
Nice to have
- Masculine Images
Should not have
- Large Cigar focus to catch customer's attention

```html
<!DOCTYPE html>
<html lang="en">
<head>
<meta charset="utf-8">
<title>Cuba Cigar Gentlemen's Memorial Day Weekend Flyer</title>
<link rel="stylesheet" href="https://fonts.googleapis.com/css2?family=Michroma&family=Roboto+Condensed:wght@400;700&display=swap">
<style>
  :root{
    --page:#ebe8e3;
    --ink:#111111;
    --gold:#d8b04a;
    --gold-light:#f2d77e;
    --gold-text:#e2c267;
    --white:#ffffff;
    --red:#c8251e;
    --red-dark:#8e1410;
  }
  *{box-sizing:border-box;margin:0;padding:0}
  html,body{width:1200px;height:800px;overflow:hidden;background:var(--page)}
  body{position:relative;font-family:"Roboto Condensed",sans-serif}
  .flyer{position:absolute;top:22px;width:540px;height:756px;background:var(--ink);overflow:hidden;box-shadow:0 4px 14px rgba(0,0,0,.25)}
  .flyer--front{left:40px}
  .flyer--back{left:620px}
  .flyer svg.art{position:absolute;left:0;top:0;width:540px;height:756px}

  /* front */
  .front-band{position:absolute;left:0;top:250px;width:540px;height:255px;
    background:linear-gradient(180deg,#1c1c1c,#0d0d0d);
    border-top:2px solid var(--gold);border-bottom:2px solid var(--gold)}
  .front-title{position:absolute;left:0;top:18px;width:540px;text-align:center;white-space:nowrap;
    font-family:"Michroma",sans-serif;font-weight:400;font-size:19px;line-height:36px;letter-spacing:1.5px;
    background:linear-gradient(180deg,var(--gold-light),#a8802a);
    -webkit-background-clip:text;background-clip:text;color:transparent}
  .front-sub{position:absolute;right:80px;top:94px;color:var(--gold-text);font-size:16px;white-space:nowrap}
  .front-info{position:absolute;left:22px;top:133px;color:var(--gold-text);font-size:11.5px;line-height:14px}
  .front-info p{margin-bottom:11px}
  .brand-row{position:absolute;left:375px;top:140px;display:flex;gap:22px}
  .brand{display:flex;flex-direction:column;align-items:center;width:64px}
  .brand-dot{width:40px;height:40px;border-radius:50%;background:var(--white)}
  .brand-name{margin-top:5px;color:var(--gold-text);font-size:11px;line-height:12px;text-align:center}
  .book-now{position:absolute;left:340px;top:676px;width:192px;height:50px;border-radius:10px;
    background:linear-gradient(180deg,var(--red),var(--red-dark));border:2px solid #e9c7a0;
    color:var(--white);font-family:"Michroma",sans-serif;font-size:11px;line-height:18px;
    letter-spacing:.5px;text-align:center;white-space:nowrap;
    display:flex;flex-direction:column;justify-content:center;align-items:center}

  /* back */
  .back-title{position:absolute;left:22px;top:22px;color:var(--gold-text);font-size:15px;font-weight:700}
  .back-body{position:absolute;left:22px;top:50px;width:498px;color:var(--gold-text);font-size:10.7px;line-height:14.4px}
  .back-details{position:absolute;left:22px;top:232px;color:var(--gold-text);font-size:11px;line-height:14.4px}
  .back-details p{margin-bottom:14px}
  .back-brands{left:295px;top:232px}
</style>
</head>
<body>

<section class="flyer flyer--front">
  <svg class="art" viewBox="0 0 540 756">
    <defs>
      <linearGradient id="dash" x1="0" y1="0" x2="1" y2="1">
        <stop offset="0" stop-color="#3a6b60"/><stop offset=".5" stop-color="#b08a4a"/><stop offset="1" stop-color="#5a4a36"/>
      </linearGradient>
      <linearGradient id="cigarTop" x1="0" y1="0" x2="1" y2="1">
        <stop offset="0" stop-color="#6e5a48"/><stop offset="1" stop-color="#7a4a2a"/>
      </linearGradient>
      <linearGradient id="glasses" x1="0" y1="0" x2="1" y2="1">
        <stop offset="0" stop-color="#6b5323"/><stop offset="1" stop-color="#b48a3c"/>
      </linearGradient>
      <linearGradient id="stall" x1="0" y1="0" x2="1" y2="1">
        <stop offset="0" stop-color="#8f8a7a"/><stop offset=".5" stop-color="#c05a1f"/><stop offset="1" stop-color="#3a2a1e"/>
      </linearGradient>
    </defs>
    <polygon role="img" aria-label="Classic car dashboard with steering wheel" points="0,0 540,0 540,40 0,250" fill="url(#dash)"/>
    <polygon role="img" aria-label="Two Cuban cigars resting on a car seat" points="540,40 540,250 0,250" fill="url(#cigarTop)"/>
    <line x1="0" y1="250" x2="540" y2="40" stroke="var(--gold)" stroke-width="2"/>
    <polygon role="img" aria-label="Row of rum glasses glowing in warm light" points="0,505 540,505 540,690" fill="url(#glasses)"/>
    <polygon role="img" aria-label="Havana street market stall with printed t-shirts" points="0,505 540,690 540,756 0,756" fill="url(#stall)"/>
    <line x1="0" y1="505" x2="540" y2="690" stroke="var(--gold)" stroke-width="2"/>
  </svg>

  <div class="front-band">
    <h1 class="front-title">A CUBA CIGAR GENTLEMEN'S<br>MEMORIAL DAY WEEKEND</h1>
    <p class="front-sub">Cigars, Rum &amp; Classic Cars...</p>
    <div class="front-info">
      <p>Legally travel to Cuba and return with real CUBAN CIGARS</p>
      <p>Trip Name: Rum Cigars and Classic Cars MEMORIAL DAY WEEKED 2018:<br>Dates: Friday, May 25th - Tuesday, May 29th</p>
      <p>Book Today at www.sampletrips.com/CUBA2018</p>
      <p>For More Information Cal: XXX-XXX-XXXX</p>
    </div>
    <div class="brand-row">
      <div class="brand"><span class="brand-dot"></span><span class="brand-name">Island Escape</span></div>
      <div class="brand"><span class="brand-dot"></span><span class="brand-name">Harbor Line Travel</span></div>
    </div>
  </div>

  <div class="book-now"><span>BOOK NOW!</span><span>SPACE IS LIMITED</span></div>
</section>

<section class="flyer flyer--back">
  <svg class="art" viewBox="0 0 540 756">
    <defs>
      <linearGradient id="car" x1="0" y1="0" x2="1" y2="1">
        <stop offset="0" stop-color="#9aa0a6"/><stop offset=".5" stop-color="#c0561c"/><stop offset="1" stop-color="#5e2208"/>
      </linearGradient>
      <linearGradient id="rum" x1="0" y1="0" x2="0" y2="1">
        <stop offset="0" stop-color="#2a1a0c"/><stop offset="1" stop-color="#8a4a16"/>
      </linearGradient>
      <linearGradient id="cigarEnds" x1="0" y1="0" x2="0" y2="1">
        <stop offset="0" stop-color="#1a140e"/><stop offset="1" stop-color="#6a4a30"/>
      </linearGradient>
    </defs>
    <polygon role="img" aria-label="Chrome grille and headlight of an orange classic car" points="540,215 271,486 540,756" fill="url(#car)"/>
    <polygon role="img" aria-label="Glass of dark rum" points="0,486 271,486 0,756" fill="url(#rum)"/>
    <polygon role="img" aria-label="Close-up of two cigar ends" points="271,486 0,756 540,756" fill="url(#cigarEnds)"/>
    <polyline points="540,215 271,486 0,486" fill="none" stroke="var(--gold)" stroke-width="2"/>
    <line x1="271" y1="486" x2="0" y2="756" stroke="var(--gold)" stroke-width="2"/>
    <line x1="271" y1="486" x2="540" y2="756" stroke="var(--gold)" stroke-width="2"/>
  </svg>

  <h2 class="back-title">Rum Cigars and Classic Cars MEMORIAL DAY WEEKED 2018</h2>
  <p class="back-body">Cuba is the ultimate bucket list destination for any cigar lover. Now is your opportunity to legally travel to Cuba and experience a country that has been off limits to Americans for more that 50 years before it changes. Smoke fine Cuban cigars, meet its resilient people and experience Cuba's fascinating culture. Tour cigar factories, watch expert cigar rollers, visit a humidor factory and workshop, tour the Old Harbor Rum Museum to learn firsthand the process of making rum followed by rum tasting and pairings with Cuban cigars in private setting and more. Explore the Pinar Del Rio located in the Viñales Valley known for its stunning landscapes and tobacco plantations. Visit the world famous Vega Verde Tobacco Plantation to see firsthand where and how the tobacco process is grown for fine Cuban cigars. The bucket list trip of a lifetime awaits on this 'people to people' Cigar journey to Cuba to learn firsthand about Cuban cigars, meet the Cuban people, experience incredible cuisine, drive in classic American cars along the Malecon and experience the Cuban cigar process from 'seed to smoke' and an opportunity to smoke in the birthplace of cigars!</p>

  <div class="back-details">
    <p>Trip Cost: $2050<br>Deposit: $300<br>Payment plans available<br>Final payment Due By April 10, 2018<br>*NON-REFUNDABLE<br>*Passport Required</p>
    <p>What's Included:<br>4 Days / 3 Nights<br>5 Star Hotel Accommodations Based on Double Occupancy<br>Roundtrip Coastal Air Tickets from Fort Lauderdale Florida - Cuba<br>Tour Bus Chauffeured Transportation<br>All Rum and Cigar Tour Events<br>Select Meals (Breakfast, Welcome and Farewell Dinner)<br>and More!</p>
    <p>For More Information Call: XXX-XXX-XXXX</p>
  </div>

  <div class="brand-row back-brands">
    <div class="brand"><span class="brand-dot"></span><span class="brand-name">Island Escape</span></div>
    <div class="brand"><span class="brand-dot"></span><span class="brand-name">Harbor Line Travel</span></div>
  </div>
</section>

</body>
</html>
```